Information poster for parquet showroom

We are a parquet shop from germany and need some information poster for our showroom, to show our costumers some important information about parqut directly. The three posters are about reasons for parquet, and there are two types of paper on the subject. We would like to place the posters in a wooden frame. The design should be modern but simple. Enclosed I send you some of my ideas but it does not have to be like this. Can be completely different. I also send you some pictures of our showroom. 1st poster: Why parquet (dimension: 90x130 cm) Why parquet? - brings nature into your home - ecologically sustainable raw material - pleasantly warm - timeless% 26amp; high quality optics - durable% 26amp; reparable flooring - improved indoor climate - unique ride 2. Advantages oiled - tangible wood structure - natural appearance - scratches less present - partial repair possible advantage varnished - very easy-care - classic% 26amp; elegant appearance - protection against dirt and moisture - variable gloss level 3. Poster: overview of the hardness of different kinds of wood (dimension: 67x130 cm) wood hardness according to Brinell in N / mm² maple europ. 28 maple canadian. 35 birch 27 beech 33 oak 34 alder 17 ash 37 doussie 42 spruce 12 kambala 30 chestnut 18 pine 20 cherry european. 31 Larch 19 Merbau 44 Robinia 48 Sucupira 57 Elm 30 Wenge 45

```html
<!DOCTYPE html>
<html lang="de">
<head>
<meta charset="utf-8">
<title>Holzhärte nach Brinell</title>
<link href="https://fonts.googleapis.com/css2?family=Alfa+Slab+One&display=swap" rel="stylesheet">
<style>
  :root {
    --backdrop: #d3d4d6;
    --charcoal: #2b2d2c;
    --amber: #f8b02d;
    --flame: #f2652d;
    --white: #ffffff;
  }
  html, body {
    margin: 0;
    padding: 0;
    width: 1200px;
    height: 1200px;
    overflow: hidden;
    background: var(--backdrop);
  }
  .poster {
    position: absolute;
    left: 308px;
    top: 34px;
    width: 584px;
    height: 1132px;
    display: block;
  }
  .poster text {
    font-family: "Alfa Slab One", "Rockwell", serif;
  }
  .title { fill: var(--amber); font-size: 88px; }
  .subtitle { fill: var(--white); font-size: 46px; }
  .wood-name, .hardness-value { fill: var(--charcoal); font-size: 38px; }
  .bar-flame { fill: var(--flame); }
  .bar-charcoal { fill: var(--charcoal); }
  .header-band { fill: var(--charcoal); }
  .chart-field { fill: var(--amber); }
</style>
</head>
<body>
<svg class="poster" viewBox="0 0 846 1640" xmlns="http://www.w3.org/2000/svg" role="img" aria-label="Holzhärte nach Brinell in N/mm²">
  <rect class="chart-field" x="0" y="0" width="846" height="1640"/>
  <rect class="header-band" x="0" y="0" width="846" height="246"/>
  <text class="title" x="423" y="124" text-anchor="middle" textLength="627" lengthAdjust="spacingAndGlyphs">HOLZHÄRTE</text>
  <text class="subtitle" x="423" y="204" text-anchor="middle" textLength="648" lengthAdjust="spacingAndGlyphs">nach Brinell in N/mm²</text>

  <g class="hardness-chart">
    <g transform="translate(0,340)"><text class="wood-name" x="68" y="14">SUCUPIRA</text><rect class="bar-flame" x="400" y="-16" width="360" height="32"/><text class="hardness-value" x="766" y="14">57</text></g>
    <g transform="translate(0,406.8)"><text class="wood-name" x="68" y="14">ROBINIE</text><rect class="bar-charcoal" x="400" y="-16" width="303" height="32"/><text class="hardness-value" x="709" y="14">48</text></g>
    <g transform="translate(0,473.6)"><text class="wood-name" x="68" y="14">WENGE</text><rect class="bar-flame" x="400" y="-16" width="284" height="32"/><text class="hardness-value" x="690" y="14">45</text></g>
    <g transform="translate(0,540.4)"><text class="wood-name" x="68" y="14">MERBAU</text><rect class="bar-charcoal" x="400" y="-16" width="278" height="32"/><text class="hardness-value" x="684" y="14">44</text></g>
    <g transform="translate(0,607.2)"><text class="wood-name" x="68" y="14">DOUSSIE</text><rect class="bar-flame" x="400" y="-16" width="265" height="32"/><text class="hardness-value" x="671" y="14">42</text></g>
    <g transform="translate(0,674)"><text class="wood-name" x="68" y="14">ESCHE</text><rect class="bar-charcoal" x="400" y="-16" width="234" height="32"/><text class="hardness-value" x="640" y="14">37</text></g>
    <g transform="translate(0,740.8)"><text class="wood-name" x="68" y="14">AHORN KAN.</text><rect class="bar-flame" x="400" y="-16" width="221" height="32"/><text class="hardness-value" x="627" y="14">35</text></g>
    <g transform="translate(0,807.6)"><text class="wood-name" x="68" y="14">EICHE</text><rect class="bar-charcoal" x="400" y="-16" width="215" height="32"/><text class="hardness-value" x="621" y="14">34</text></g>
    <g transform="translate(0,874.4)"><text class="wood-name" x="68" y="14">BUCHE</text><rect class="bar-flame" x="400" y="-16" width="208" height="32"/><text class="hardness-value" x="614" y="14">33</text></g>
    <g transform="translate(0,941.2)"><text class="wood-name" x="68" y="14">KIRSCHE EUR.</text><rect class="bar-charcoal" x="400" y="-16" width="196" height="32"/><text class="hardness-value" x="602" y="14">31</text></g>
    <g transform="translate(0,1008)"><text class="wood-name" x="68" y="14">KAMBALA</text><rect class="bar-flame" x="400" y="-16" width="189" height="32"/><text class="hardness-value" x="595" y="14">30</text></g>
    <g transform="translate(0,1074.8)"><text class="wood-name" x="68" y="14">ULME</text><rect class="bar-charcoal" x="400" y="-16" width="189" height="32"/><text class="hardness-value" x="595" y="14">30</text></g>
    <g transform="translate(0,1141.6)"><text class="wood-name" x="68" y="14">AHORN EUR.</text><rect class="bar-flame" x="400" y="-16" width="177" height="32"/><text class="hardness-value" x="583" y="14">28</text></g>
    <g transform="translate(0,1208.4)"><text class="wood-name" x="68" y="14">BIRKE</text><rect class="bar-charcoal" x="400" y="-16" width="171" height="32"/><text class="hardness-value" x="577" y="14">27</text></g>
    <g transform="translate(0,1275.2)"><text class="wood-name" x="68" y="14">KIEFER</text><rect class="bar-flame" x="400" y="-16" width="126" height="32"/><text class="hardness-value" x="532" y="14">20</text></g>
    <g transform="translate(0,1342)"><text class="wood-name" x="68" y="14">LÄRCHE</text><rect class="bar-charcoal" x="400" y="-16" width="120" height="32"/><text class="hardness-value" x="526" y="14">19</text></g>
    <g transform="translate(0,1408.8)"><text class="wood-name" x="68" y="14">KASTANIE</text><rect class="bar-flame" x="400" y="-16" width="114" height="32"/><text class="hardness-value" x="520" y="14">18</text></g>
    <g transform="translate(0,1475.6)"><text class="wood-name" x="68" y="14">ERLE</text><rect class="bar-charcoal" x="400" y="-16" width="107" height="32"/><text class="hardness-value" x="513" y="14">17</text></g>
    <g transform="translate(0,1542.4)"><text class="wood-name" x="68" y="14">FICHTE</text><rect class="bar-flame" x="400" y="-16" width="76" height="32"/><text class="hardness-value" x="482" y="14">12</text></g>
  </g>
</svg>
</body>
</html>
```